Coastal Bright Sweep Business Card

We are a cleaning and waste management company with the slogan "making waste to landfill a thing of the past". We would like a re-design of our current business card. On the front we want to continue to use our logo as the focus point. On the back, we want the whole thing re-done to be less busy. We want the staff member’s name, the job title, mobile number, email and website. We do not want the address on the card. We still want the green, black and blue colours used, but a new font for the information on the back. Please do not change the logo design at all. We are also thinking about using icons to replace the text ‘mobile, email, website’. The “events + commercial” banner needs to be incorporated somewhere and needs to read “events + commercial + waste”. Another important point for consideration is that we are very concerned about being environmentally sustainable and will be printing on recycled paper. All designs should be made to compliment this in regards to boldness and colouring. Please find attached our logo, our colour chart and an image of our current business card.

```html
<!DOCTYPE html>
<html lang="en">
<head>
<meta charset="utf-8">
<title>Coastal Bright Sweep – Business Card</title>
<link href="https://fonts.googleapis.com/css2?family=Arimo:wght@400;700&display=swap" rel="stylesheet">
<style>
  :root {
    --stage: #1c1c1c;
    --paper: #ffffff;
    --navy: #0f3a6b;
    --leaf: #7dc242;
    --sky: #1aa3e0;
    --ink: #1a1a1a;
    --rule: #8a8f96;
    --grad-top: #2bb5e6;
    --grad-mid: #7dc242;
    --grad-low: #3f9a4a;
    --grad-end: #0e3f72;
  }
  * { margin: 0; padding: 0; box-sizing: border-box; }
  html, body {
    width: 1200px; height: 900px; overflow: hidden;
    background: var(--stage);
    font-family: "Arimo", Arial, sans-serif;
  }
  .card {
    position: absolute;
    top: 170px;
    width: 347px; height: 561px;
    box-shadow: 3px 4px 6px rgba(0,0,0,0.55);
  }
  .card--info { left: 259px; background: var(--paper); }
  .card--brand {
    left: 631px;
    background: linear-gradient(160deg, var(--grad-top) 0%, var(--grad-mid) 45%, var(--grad-low) 72%, var(--grad-end) 100%);
    overflow: hidden;
  }
  .card__pattern { position: absolute; inset: 0; }

  .wordmark {
    position: absolute; left: 0; right: 0;
    text-align: center;
    font-weight: 700;
    line-height: 1;
  }
  .card--info .wordmark { top: 110px; color: var(--sky); }
  .card--brand .wordmark { top: 210px; color: #ffffff; }
  .wordmark span { display: block; }
  .wordmark__line-sm { font-size: 26px; letter-spacing: 2px; margin-bottom: 6px; }
  .wordmark__line-lg { font-size: 52px; letter-spacing: -1px; }

  .person {
    position: absolute; top: 360px; left: 0; right: 0;
    text-align: center;
  }
  .person__name { font-size: 20px; font-weight: 700; letter-spacing: 0.3px; }
  .person__first { color: var(--leaf); }
  .person__last { color: var(--sky); }
  .person__role { font-size: 15px; color: var(--ink); margin-top: 2px; }

  .contact-icons {
    position: absolute; top: 438px; left: 96px;
    width: 156px; height: 16px;
  }
  .contact {
    position: absolute; top: 460px; left: 0; right: 0;
    text-align: center; font-size: 15.5px; line-height: 20.5px; color: var(--ink);
  }
</style>
</head>
<body>

<section class="card card--info" aria-label="Business card, contact side">
  <h1 class="wordmark">
    <span class="wordmark__line-sm">COASTAL</span>
    <span class="wordmark__line-lg">Bright</span>
    <span class="wordmark__line-lg">Sweep</span>
  </h1>

  <div class="person">
    <p class="person__name"><span class="person__first">MORGAN</span> <span class="person__last">ELLERY</span></p>
    <p class="person__role">Client Manager</p>
  </div>

  <svg class="contact-icons" viewBox="0 0 156 16" aria-hidden="true">
    <line x1="0" y1="8" x2="48" y2="8" stroke="var(--rule)" stroke-width="1"/>
    <line x1="108" y1="8" x2="156" y2="8" stroke="var(--rule)" stroke-width="1"/>
    <!-- phone -->
    <g fill="var(--navy)">
      <path d="M50 6 q8 -5 16 0 v2 h-4 v-1.5 q-4 -1.5 -8 0 v1.5 h-4z"/>
      <rect x="53" y="9" width="10" height="6" rx="1"/>
    </g>
    <!-- mail -->
    <rect x="72" y="3" width="14" height="10" fill="var(--leaf)"/>
    <path d="M72 3 l7 6 l7 -6" fill="none" stroke="#ffffff" stroke-width="1"/>
    <!-- globe -->
    <circle cx="99" cy="8" r="6.5" fill="var(--sky)"/>
    <path d="M95 5 q3 -1 4 2 q-2 2 0 4 M101 3 q2 3 1 6" fill="none" stroke="#ffffff" stroke-width="1"/>
  </svg>

  <address class="contact" style="font-style:normal">
    <p>0400 555 218</p>
    <p>mellery@coastalbrightsweep.com.au</p>
    <p>www.coastalbrightsweep.com.au</p>
  </address>
</section>

<section class="card card--brand" aria-label="Business card, brand side">
  <div class="card__pattern" role="img" aria-label="Scattered faint star pattern over a blue to green gradient"></div>
  <p class="wordmark">
    <span class="wordmark__line-sm">COASTAL</span>
    <span class="wordmark__line-lg">Bright</span>
    <span class="wordmark__line-lg">Sweep</span>
  </p>
</section>

</body>
</html>
```